We need a book cover design for a fitness professional's guidebook to be a successful trainer. LA celebrity trainer offers 7 ideas that are designed to transform any fitness professional's career and life. The cover design we are into is attached an includes the image of a man who is half dressed in a business suit and half dressed in fitness gear. The back photo should demonstrate the four sphere's the book is designed around (also attached) and will be included on the back with a brief description of the material (included below) and a short bio and photo of the writer (attached) at the very bottom. We'd like the book to have a work book feel, or text book geometry to it. The brand colors are Black and Red. The final design should invoke the feeling of success, health and happiness.

Dimensions: 8 5/8 x 5 3/4

USE WEBSITE AS REFERENCE FOR BRAND COLORS AND DESIGNS:
BravoMotion.net

BOOK TITLE:
RISING STRIDE
"A fitness professional's guidebook to be a successful trainer."

BACK COVER COPY:
Celebrity conditioning specialist and trainer consultant, Tavo Quintero, offers powerful ideas that are designed to transform every fitness professional's career and life. Reveal essential tools that every trainer and entrepreneur should know. Discover the deeper meaning of yourself and your career by working smarter rather than harder.

Find out how to create a brand, advertise it, and hone in on your market. Create buzz by landing magazine press. How to build celebrity clientele. Explore the world of multi-media projects. And finally, what to do when you reach your goals. This is an opportunity for trainer's to capture a share of the fitness industry’s vast $27B market. Fulfill your fullest earning potential while also understanding what the true meaning of success is, and how to achieve it. Learn what you love to do, what you do well, what the fitness industry needs and what it will pay for.

Aimed at the trainers who want to know the mistakes to avoid, and the habits to establish that will set them apart from the rest, Rising Stride is THE guidebook that has the power to take your career and life in the direction that will prepare you for continued success. Use these business ideas to promote your passive income, generate multiple streams of revenue and increase your investments, resulting in more freedom and access in the fitness industry and beyond. Let Rising Stride unleash your potential to be a successful trainer.

BACK AUTHOR BIO:
Los Angeles based celebrity trainer and trainer consultant, Tavo Quintero, CSCS, developed his very own “Anchor” technique and fitness brand. Quintero’s clients include a mix of celebrities, professional athletes, musicians, fashion models, students, political figures and corporate professionals. Vigor magazine described Quintero’s fitness DVD, TAVOMOVE, as “a workout you’ll look forward to”. Tavo was also the co-developer of a natural energy drink that increases energy and metabolism with an ancient Peruvian super food. Additionally backed by his finance and advertising education, Tavo has consulted several trainers and fitness brands to guide them to their maximum earning potential.

Target Market(s)

Fitness Industry/Trainers

Industry/Entity Type

Advertising

Requirements
Must have
• Consistent with website logo colors, shapes and fonts.

```html
<!DOCTYPE html>
<html lang="en">
<head>
<meta charset="utf-8">
<title>Rising Stride — Book Cover</title>
<link rel="stylesheet" href="https://fonts.googleapis.com/css2?family=Open+Sans:wght@300;400;700&display=swap">
<style>
  :root {
    --ink-black: #0d0d0d;
    --brand-red: #e3211f;
    --paper: #f7f7f7;
    --paper-shade: #e9e9e9;
    --subtitle-grey: #4a4a4a;
    --stage: #e4e2df;
    --white: #ffffff;
    --suit-grey: #4b4b4b;
    --skin-tone: #d9b49a;
  }
  * { box-sizing: border-box; margin: 0; padding: 0; }
  html, body {
    width: 1081px;
    height: 1200px;
    overflow: hidden;
    background: var(--stage);
    font-family: "Open Sans", Arial, sans-serif;
  }
  .book {
    position: absolute;
    left: 160px;
    top: 70px;
    width: 760px;
    height: 1060px;
    display: flex;
  }

  /* Spine */
  .spine {
    position: relative;
    width: 60px;
    height: 100%;
    background: linear-gradient(90deg, #f2f2f2 0%, var(--white) 60%, #e6e6e6 100%);
    overflow: hidden;
  }
  .spine-top {
    position: absolute;
    left: 0; top: 0;
    width: 100%;
    height: 300px;
    background: var(--ink-black);
  }
  .spine-author {
    position: absolute;
    left: 0; right: 0; top: 24px;
    margin: 0 auto;
    writing-mode: vertical-rl;
    color: var(--brand-red);
    font-weight: 700;
    font-size: 20px;
    letter-spacing: 2px;
    line-height: 60px;
    width: 60px;
  }
  .spine-rule {
    position: absolute;
    left: 0; top: 300px;
    width: 100%;
    height: 10px;
    background: var(--brand-red);
  }
  .spine-title {
    position: absolute;
    left: 0; top: 470px;
    width: 60px;
    writing-mode: vertical-rl;
    color: var(--ink-black);
    font-size: 26px;
    line-height: 60px;
    letter-spacing: 2px;
    white-space: nowrap;
  }
  .spine-title .light { font-weight: 300; }
  .spine-title .bold { font-weight: 700; margin-top: 10px; }
  .spine-bottom {
    position: absolute;
    left: 0; bottom: 0;
    width: 100%;
    height: 118px;
    background: var(--brand-red);
  }

  /* Front cover */
  .front-cover {
    position: relative;
    width: 700px;
    height: 100%;
    background: linear-gradient(90deg, var(--paper-shade) 0%, var(--paper) 25%, var(--white) 100%);
    box-shadow: inset 4px 0 6px rgba(0,0,0,0.12);
    overflow: hidden;
  }
  .title-band {
    position: absolute;
    left: 0; top: 0;
    width: 100%;
    height: 300px;
    background: var(--ink-black);
    color: var(--white);
    text-align: center;
  }
  .title-light {
    position: absolute;
    left: 0; right: 0; top: 14px;
    font-weight: 300;
    font-size: 138px;
    line-height: 1;
    letter-spacing: -2px;
  }
  .title-bold {
    position: absolute;
    left: 0; right: 0; top: 150px;
    font-weight: 700;
    font-size: 128px;
    line-height: 1;
    letter-spacing: -2px;
  }
  .accent-rule {
    position: absolute;
    left: 0; top: 300px;
    width: 100%;
    height: 10px;
    background: var(--brand-red);
  }
  .subtitle {
    position: absolute;
    left: 0; right: 0; top: 330px;
    text-align: center;
    color: var(--subtitle-grey);
    font-weight: 400;
    font-size: 25px;
    line-height: 1.3;
    letter-spacing: 1.5px;
  }
  .author-portrait {
    position: absolute;
    left: 230px; top: 410px;
    width: 240px;
    height: 530px;
    border-radius: 120px 120px 18px 18px;
    background:
      linear-gradient(180deg, rgba(217,180,154,0.9) 0%, rgba(217,180,154,0) 18%),
      linear-gradient(90deg, #2a2a2a 0%, var(--brand-red) 22%, var(--brand-red) 48%, var(--suit-grey) 52%, #3a3a3a 100%);
    opacity: 0.88;
  }
  .author-band {
    position: absolute;
    left: 0; bottom: 0;
    width: 100%;
    height: 118px;
    background: var(--brand-red);
    color: var(--white);
    text-align: center;
    font-weight: 700;
    font-size: 36px;
    line-height: 118px;
    letter-spacing: 0.5px;
  }
</style>
</head>
<body>
  <div class="book">
    <aside class="spine">
      <div class="spine-top"></div>
      <span class="spine-author">TAVO QUINTERO</span>
      <div class="spine-rule"></div>
      <p class="spine-title"><span class="light">RISING</span> <span class="bold">STRIDE</span></p>
      <div class="spine-bottom"></div>
    </aside>
    <main class="front-cover">
      <header class="title-band">
        <h1>
          <span class="title-light">RISING</span>
          <span class="title-bold">STRIDE</span>
        </h1>
      </header>
      <div class="accent-rule"></div>
      <p class="subtitle">A FITNESS PROFESSIONAL'S GUIDEBOOK<br>TO BE A SUCCESSFUL TRAINER</p>
      <div class="author-portrait" role="img" aria-label="Full-length photo of a smiling man, half in a business suit and tie, half in red and black cycling gear"></div>
      <footer class="author-band">TAVO QUINTERO</footer>
    </main>
  </div>
</body>
</html>
```